DORLIT HOMES Professional Home Buyers

Please see two files uploaded. One is my new LOGO (thanks Quenby) and the other gives the wording and pages desired. Of course I am open to suggestions to further enhance what I'm about. I don't want testimonials or houses to buy to appear but to have room for them when I'm ready. I am a real estate investor not a licensed real estate agent. For FAQ i want just the questions to appear and when they click on the question the answer appears and when they click on the question again the answer disappears. make sense? When you read my wording and my idea of pages you'll get an idea of what I'm about. Suggestions are welcomed.

Industry/Entity Type

Real Estate

Number of Pages Required

5+ page

Requirements
Must have
• FAQ pages only questions appear. They click on question the answer appears underneath. they click on question again, the answer disappears. Also, I of course, want my new LOGO to appear on each page I don't know if it will look better all by itself or blended in somehow? Call now 418-555-0193 on each page also. I will get a real phone number before website goes live. If you have a better way of wording what I'm describing please let me know, I am open to feedback
Nice to have
• Anything that the average homeowner can relate to (yea I know, that doesn't help you much, right?)
• Testimonial page and houses to buy page could be done with just the shell ready in the wings for when my business grows it will be ready all that it would need then are the wording and pictures to be uploaded onto the website page. make sense?
Should not have
• I don't want it too elegant or rich looking as I believe my audience will be mostly the average homeowner who needs help

```html
<!DOCTYPE html>
<html lang="en">
<head>
<meta charset="utf-8">
<title>DORLIT HOMES – Professional Home Buyers</title>
<link href="https://fonts.googleapis.com/css2?family=Open+Sans:wght@300;400;600;700&display=swap" rel="stylesheet">
<style>
:root{
  --navy:#0b3a73;
  --blue:#1763b0;
  --sky:#2f86d0;
  --ink:#2b2f36;
  --muted:#7a808a;
  --rule:#e3e6ea;
  --band:#eef1f4;
  --white:#ffffff;
}
*{box-sizing:border-box;margin:0;padding:0}
html,body{width:870px;height:1200px;overflow:hidden;background:var(--white)}
body{font-family:"Open Sans",Arial,sans-serif;color:var(--ink);position:relative}
.page{position:relative;width:870px;height:1200px}

/* header */
.site-header{position:absolute;top:0;left:0;width:870px;height:100px;background:var(--white)}
.nav-bar{position:absolute;top:62px;left:320px;right:0;height:30px;background:var(--navy)}
.main-nav{position:absolute;top:0;left:12px;display:flex;gap:16px;height:30px;align-items:center}
.main-nav a{color:var(--white);font-size:10px;font-weight:600;text-decoration:none;letter-spacing:.3px;white-space:nowrap}
.call-now{position:absolute;top:10px;right:140px;text-align:right;color:var(--navy)}
.call-now .label{font-size:11px;font-weight:700;letter-spacing:1px;color:var(--blue)}
.call-now .phone{font-size:17px;font-weight:700;display:flex;align-items:center;gap:5px}
.logo{position:absolute;top:0;left:140px;width:170px;height:110px;background:var(--white);
  box-shadow:0 2px 6px rgba(0,0,0,.18);z-index:3;display:flex;flex-direction:column;align-items:center;justify-content:center;gap:6px}
.logo .mark{width:14px;height:14px;background:var(--navy)}
.logo .name{font-size:21px;font-weight:700;color:var(--navy);letter-spacing:.5px;white-space:nowrap}
.logo .tag{font-size:8px;font-weight:600;color:var(--muted);letter-spacing:1px;text-transform:uppercase}

/* hero */
.hero{position:absolute;top:92px;left:0;width:870px;height:313px;overflow:hidden}
.hero-photo{position:absolute;inset:0;
  background:
    radial-gradient(ellipse 160px 220px at 160px 150px,rgba(60,70,80,.35),transparent 70%),
    radial-gradient(ellipse 180px 240px at 640px 160px,rgba(50,60,70,.35),transparent 70%),
    linear-gradient(180deg,rgba(255,255,255,.25),rgba(0,0,0,.1)),
    linear-gradient(100deg,#b9a891 0%,#ddd3c2 28%,#b3c49c 58%,#6f8c62 100%)}
.hero-box{position:absolute;left:150px;top:165px;padding:10px 16px 12px;background:rgba(11,58,115,.85);color:var(--white);white-space:nowrap}
.hero-box p{font-size:14px;line-height:1.35}
.hero-box strong{display:block;font-size:21px;font-weight:700;margin-top:3px}

/* intro */
.intro{position:absolute;top:430px;left:140px;width:590px;text-align:center}
.intro h1{font-size:24px;font-weight:400;color:var(--ink)}
.intro p{font-size:9px;color:var(--muted);line-height:1.55;margin-top:10px}
.btn{display:inline-block;background:var(--navy);color:var(--white);font-size:11px;font-weight:600;padding:8px 18px;text-decoration:none;border-radius:2px}
.intro .btn{margin-top:18px}

/* cash band */
.cash{position:absolute;top:600px;left:0;width:870px;height:210px;background:linear-gradient(180deg,#f6f7f9,#e9edf1)}
.cash-text{position:absolute;left:140px;top:50px;width:280px}
.section-title{font-size:18px;font-weight:400;color:var(--blue);text-transform:uppercase;white-space:nowrap}
.cash-text p{font-size:9px;color:var(--muted);line-height:1.55;margin-top:8px}
.cash-text .btn{margin-top:14px}
.cash-photo{position:absolute;left:470px;top:30px;width:260px;height:160px;
  background:
    radial-gradient(ellipse 90px 60px at 70px 110px,rgba(150,160,120,.55),transparent 75%),
    radial-gradient(ellipse 120px 70px at 190px 60px,rgba(240,236,226,.9),transparent 75%),
    linear-gradient(135deg,#c9d2db,#eeebe2 50%,#a4b293)}

/* sell section */
.sell-photo{position:absolute;left:140px;top:880px;width:295px;height:165px;
  background:
    radial-gradient(ellipse 110px 70px at 150px 90px,rgba(240,240,240,.7),transparent 75%),
    radial-gradient(ellipse 80px 60px at 60px 110px,rgba(120,140,170,.45),transparent 75%),
    linear-gradient(135deg,#e7ddd0,#c9b7a1 60%,#8e9fb2)}
.sell-text{position:absolute;left:478px;top:835px;width:255px}
.sell-text p{font-size:9px;color:var(--muted);line-height:1.55;margin-top:6px}
.checklist{list-style:none;margin-top:12px}
.checklist li{font-size:9.5px;color:var(--ink);display:flex;align-items:center;gap:7px;margin-bottom:7px}

/* footer */
.site-footer{position:absolute;top:1125px;left:0;width:870px;height:75px;border-top:1px solid var(--rule);background:#f8f9fa}
.footer-nav{position:absolute;left:140px;top:22px;display:flex;gap:10px}
.footer-nav a{font-size:9px;font-weight:600;color:var(--navy);text-decoration:none;white-space:nowrap}
.copyright{position:absolute;left:140px;top:42px;font-size:8px;color:var(--muted)}
.social{position:absolute;right:140px;top:16px;display:flex;gap:6px}
.social span{width:22px;height:22px;border-radius:50%;background:var(--sky)}
</style>
</head>
<body>
<div class="page">
  <header class="site-header">
    <div class="logo">
      <span class="mark"></span>
      <span class="name">DORLIT HOMES</span>
      <span class="tag">Professional Home Buyers</span>
    </div>
    <div class="call-now">
      <div class="label">CALL NOW</div>
      <div class="phone">
        <svg width="14" height="14" viewBox="0 0 24 24"><path fill="#0b3a73" d="M6.6 10.8c1.4 2.8 3.8 5.1 6.6 6.6l2.2-2.2c.3-.3.7-.4 1-.2 1.1.4 2.3.6 3.6.6.6 0 1 .4 1 1V20c0 .6-.4 1-1 1C10.6 21 3 13.4 3 4c0-.6.4-1 1-1h3.5c.6 0 1 .4 1 1 0 1.3.2 2.5.6 3.6.1.3 0 .7-.2 1z"/></svg>
        418-555-0193
      </div>
    </div>
    <div class="nav-bar">
      <nav class="main-nav">
        <a href="#">HOME</a><a href="#">ABOUT US</a><a href="#">FAQ</a><a href="#">CONTACT US</a><a href="#">TESTIMONIALS</a><a href="#">HOUSES TO BUY</a>
      </nav>
    </div>
  </header>

  <section class="hero">
    <div class="hero-photo" role="img" aria-label="Photo of a couple receiving house keys in front of a home for sale"></div>
    <div class="hero-box">
      <p>DORLIT HOMES will buy your house AS IS,</p>
      <strong>FAST and HASSLE FREE!</strong>
    </div>
  </section>

  <section class="intro">
    <h1>We buy houses in any condition!</h1>
    <p>We don't need repairs, agents or costly inspections. DORLIT HOMES is a local company buying houses throughout the area. We buy houses fast, as is, and pay a fair cash price.<br>Contact us today for your free no obligation offer.</p>
    <a class="btn" href="#">Get your free Quote</a>
  </section>

  <section class="cash">
    <div class="cash-text">
      <h2 class="section-title">Get cash for your house!</h2>
      <p>DORLIT HOMES buys homes in any condition in your area. No fees, no commissions and no waiting on banks – just a fair cash offer.</p>
      <a class="btn" href="#">Get More Info</a>
    </div>
    <div class="cash-photo" role="img" aria-label="Photo of a hand holding cash in front of a house"></div>
  </section>

  <div class="sell-photo" role="img" aria-label="Photo of a family relaxing together at home"></div>
  <section class="sell-text">
    <h2 class="section-title">Sell your home fast!</h2>
    <p>Facing foreclosure, a move or a house that needs too much work? We make selling simple and fast.</p>
    <ul class="checklist">
      <li><svg width="11" height="11" viewBox="0 0 12 12"><rect width="12" height="12" rx="2" fill="#1763b0"/><path d="M3 6.2l2 2 4-4.4" stroke="#fff" stroke-width="1.6" fill="none"/></svg>We pay all cash</li>
      <li><svg width="11" height="11" viewBox="0 0 12 12"><rect width="12" height="12" rx="2" fill="#1763b0"/><path d="M3 6.2l2 2 4-4.4" stroke="#fff" stroke-width="1.6" fill="none"/></svg>We pay closing costs</li>
      <li><svg width="11" height="11" viewBox="0 0 12 12"><rect width="12" height="12" rx="2" fill="#1763b0"/><path d="M3 6.2l2 2 4-4.4" stroke="#fff" stroke-width="1.6" fill="none"/></svg>We buy "as is"</li>
      <li><svg width="11" height="11" viewBox="0 0 12 12"><rect width="12" height="12" rx="2" fill="#1763b0"/><path d="M3 6.2l2 2 4-4.4" stroke="#fff" stroke-width="1.6" fill="none"/></svg>No waiting for bank approvals</li>
      <li><svg width="11" height="11" viewBox="0 0 12 12"><rect width="12" height="12" rx="2" fill="#1763b0"/><path d="M3 6.2l2 2 4-4.4" stroke="#fff" stroke-width="1.6" fill="none"/></svg>Quick closings</li>
    </ul>
  </section>

  <footer class="site-footer">
    <nav class="footer-nav">
      <a href="#">HOME</a><a href="#">ABOUT US</a><a href="#">FAQ</a><a href="#">CONTACT US</a><a href="#">TESTIMONIALS</a><a href="#">HOUSES TO BUY</a>
    </nav>
    <p class="copyright">© 2016 Dorlit Homes. All rights reserved.</p>
    <div class="social"><span></span><span></span><span></span><span></span></div>
  </footer>
</div>
</body>
</html>
```